Yacht, Boats, Watersports company needs a redesign of business card

Hello Designers!
We are a Boat dealership company that sells fun in the water, we sell boats, Yachts, Kayaks and also yacht WaterSport toys. We are looking to redesign our business cards in to something a little bit more sophisticated. in a way that we can make better use of our company colors. I'm attaching a zipped file containing the company 3 sets of company logo which one is an horizontal another one is a vertical and also a chromed 3d logo. Also is included two set of business cards that we use and also some designs that i think it's interesting. We use PMS 2026c Orange and PMS 7687C Blue. I would like to see at least two different options with the orange as accent and also using blue as an accent color. It's really important for the business cards to have a font option and size that is legible to most people. Our current website is wwww.coralpiermarine.com. Please visit if you want to have a better feeling of the Boat dealership
You can send Single sided or double side options. We are now using single sided but we may be open for a double side option if we really like the design.
Target Market(s)
Marine, boat sales, yacht sales, water toys sales/
Contact Information for Business Card
Name: Dale Whitcombe
Address: 72 North Pellham Avenue,
Palmetto Shoals, SC 33871
Phone: 954-318-4471
Fax: 954:318-4472
Cell: 954-732-1184
Email: sales@coralpiermarine.com
Website: coralpiermarine.com
Requirements
Must have
- the current information of the business card provided.
logo
use the PMS Colors
Nice to have
- a touch of elegance and sophistication but simple
Should not have
- should not have any typography that is hard to read, the card should be simple but yet sophisticated.

```html
<!DOCTYPE html>
<html lang="en">
<head>
<meta charset="utf-8">
<title>Coral Pier Marine – Business Card</title>
<link href="https://fonts.googleapis.com/css2?family=Montserrat:wght@400;500;700;800&display=swap" rel="stylesheet">
<style>
  :root{
    --brand-blue:#1d4f8c;
    --brand-blue-deep:#163f72;
    --brand-orange:#f0652a;
    --ink:#3b3f46;
    --paper:#ffffff;
    --backdrop:#e9ebee;
  }
  *{box-sizing:border-box;margin:0;padding:0}
  html,body{width:1200px;height:881px;overflow:hidden;background:var(--backdrop);font-family:"Montserrat",sans-serif}
  .stage{position:relative;width:1200px;height:881px}
  .card{position:absolute;left:290px;width:620px;height:354px;border-radius:18px;overflow:hidden;box-shadow:0 10px 28px rgba(0,0,0,.18)}
  .card--back{top:64px}
  .card--front{top:458px;background:var(--paper)}

  /* back */
  .back-pattern{position:absolute;inset:0;background:linear-gradient(135deg,#2a5f9e 0%,var(--brand-blue) 55%,var(--brand-blue-deep) 100%)}
  .back-name{position:absolute;inset:0;display:flex;align-items:center;justify-content:center;color:#fff;font-weight:800;font-size:30px;letter-spacing:5px;text-transform:uppercase}

  /* front */
  .brand{position:absolute;left:38px;top:40px;display:flex;align-items:center;gap:12px}
  .brand-dot{width:34px;height:34px;border-radius:50%;background:var(--brand-orange)}
  .brand-name{color:var(--brand-blue);font-weight:800;font-size:21px;letter-spacing:2px;text-transform:uppercase}

  .holder{position:absolute;right:36px;top:96px;color:var(--brand-blue);font-weight:800;font-size:25px;letter-spacing:2px;text-transform:uppercase;white-space:nowrap}
  .rule{position:absolute;height:1.5px;background:var(--brand-orange)}
  .rule--name{left:300px;right:30px;top:134px}
  .rule--contacts{left:40px;width:250px;top:184px}

  .contacts{position:absolute;left:40px;top:196px;list-style:none}
  .contacts li{display:flex;align-items:center;gap:10px;height:22px;font-size:15.5px;color:var(--ink);letter-spacing:.6px;white-space:nowrap}
  .contacts svg{width:13px;height:13px;flex:none}
  .contacts .domain{color:var(--brand-blue);font-weight:500}

  .address{position:absolute;right:36px;top:176px;text-align:right;font-size:14.5px;line-height:21px;color:var(--ink);letter-spacing:.6px;white-space:nowrap}

  .footer-wave{position:absolute;left:0;bottom:0;width:620px;height:100px}
</style>
</head>
<body>
<main class="stage">

  <section class="card card--back" aria-label="Card back">
    <div class="back-pattern" role="img" aria-label="Blue background with a repeating pattern of faint circular marks"></div>
    <div class="back-name">Coral Pier Marine</div>
  </section>

  <section class="card card--front" aria-label="Card front">
    <div class="brand">
      <span class="brand-dot"></span>
      <span class="brand-name">Coral Pier Marine</span>
    </div>

    <h1 class="holder">Dale Whitcombe</h1>
    <div class="rule rule--name"></div>
    <div class="rule rule--contacts"></div>

    <ul class="contacts">
      <li><svg viewBox="0 0 16 16" fill="var(--brand-orange)"><path d="M3 1l3 3-1.5 2c1 2 3 4 5 5L11.5 9.5l3 3-2 2.5C6 14 1.5 9 1 3z"/></svg><span>954-318-4471</span></li>
      <li><svg viewBox="0 0 16 16" fill="var(--brand-orange)"><rect x="4" y="1" width="8" height="4"/><rect x="1" y="6" width="14" height="6" rx="1"/><rect x="4" y="10" width="8" height="5"/></svg><span>954:318-4472</span></li>
      <li><svg viewBox="0 0 16 16" fill="none" stroke="var(--brand-orange)" stroke-width="1.6"><rect x="4" y="1" width="8" height="14" rx="1.5"/><line x1="7" y1="12.5" x2="9" y2="12.5"/></svg><span>954-732-1184</span></li>
      <li><svg viewBox="0 0 16 16" fill="none" stroke="var(--brand-orange)" stroke-width="1.6"><rect x="1" y="3" width="14" height="10" rx="1"/><path d="M1 3l7 6 7-6"/></svg><span>sales@coralpiermarine.com</span></li>
      <li><svg viewBox="0 0 16 16" fill="none" stroke="var(--brand-orange)" stroke-width="1.3"><circle cx="8" cy="8" r="6.5"/><ellipse cx="8" cy="8" rx="3" ry="6.5"/><line x1="1.5" y1="8" x2="14.5" y2="8"/></svg><span>www.<span class="domain">coralpiermarine.com</span></span></li>
    </ul>

    <p class="address">72 North Pellham Avenue,<br>Palmetto Shoals, SC 33871</p>

    <svg class="footer-wave" viewBox="0 0 620 100" preserveAspectRatio="none" aria-hidden="true">
      <path d="M380 100 C420 40 450 30 520 22 L620 10 L620 100 Z" fill="var(--brand-blue)"/>
      <path d="M0 78 L390 54 C400 53 405 55 398 60 L0 86 Z" fill="var(--brand-orange)"/>
      <path d="M0 90 L620 60 L620 100 L0 100 Z" fill="var(--brand-blue)"/>
    </svg>
  </section>

</main>
</body>
</html>
```